DJ company new brochure of services offered

I would like to get a new price sheet made for my company services. Currently it's text only. I would like to add pictures next to each service description also like to add general background colors, and just make it look more attractive overall.

Uplighting - File #4 & file #10
Centerpiece pin-spots - File #15
Wedding Cake Spot - file #13 (can you crop out the logo at the bottom)?
Dance Floor Decal File #5
Gobo Monogram - File # 3
market lighting - file #14
ballroom draping - file #7
Video/projections screens: File #13
Indoor safe sparkler effect (not listed on price sheet yet) File #11
Dancing on a cloud - File #9
Co2 Cannons - File #6

Target Market(s)

bride and grooms

Industry/Entity Type

Entertainment

Font styles to use
Serif

Colors

Designer to choose colors to be used in the design.

Requirements
Must have
• my website is www.brightloomevents.example
• instagram is: @brightloomevents.example

```html
<!DOCTYPE html>
<html lang="en">
<head>
<meta charset="utf-8">
<title>Brightloom Events – Wedding Reception Price Sheet</title>
<link href="https://fonts.googleapis.com/css2?family=EB+Garamond:wght@400;600&family=Libre+Baskerville:wght@400;700&display=swap" rel="stylesheet">
<style>
  :root{
    --paper:#ffffff;
    --ink:#2b2b2b;
    --band:#4a4a4c;
    --band-dark:#3d3d3f;
    --price:#d8201f;
    --accent:#e0282a;
    --white:#ffffff;
    --hero-a:#1d2430;
    --hero-b:#5b6678;
  }
  *{box-sizing:border-box;margin:0;padding:0}
  html,body{width:862px;height:1200px;overflow:hidden;background:var(--paper)}
  body{position:relative;font-family:"EB Garamond",Georgia,serif;color:var(--ink)}
  .abs{position:absolute}

  .hero{left:25px;top:24px;width:811px;height:198px;
    background:radial-gradient(ellipse at 55% 40%,#7d8596 0%,var(--hero-b) 35%,var(--hero-a) 100%)}
  .hero-haze{left:25px;top:150px;width:811px;height:72px;
    background:linear-gradient(to bottom,rgba(220,225,235,0),rgba(220,225,235,.35))}
  .brand{left:50px;top:98px;display:flex;align-items:center;gap:8px;
    font-family:"Libre Baskerville",Georgia,serif;font-size:21px;color:var(--white)}
  .brand-dot{width:12px;height:12px;border-radius:50%;background:var(--accent)}
  .contact{right:42px;top:70px;text-align:right;font-family:"Libre Baskerville",Georgia,serif;
    font-weight:700;font-size:11.5px;line-height:16.5px;color:var(--white)}
  .services-line{left:25px;width:811px;top:176px;text-align:center;color:var(--white);
    font-family:"Libre Baskerville",Georgia,serif;font-weight:700;font-size:17px;letter-spacing:.3px}

  .package-band{left:25px;top:222px;width:811px;height:40px;background:var(--band);
    color:var(--white);font-family:"Libre Baskerville",Georgia,serif;font-size:16px;
    display:flex;align-items:center;justify-content:center}

  .includes{left:100px;width:410px;top:282px;text-align:center;font-size:15px;line-height:19.7px}
  .includes h2{font-size:15.5px;font-weight:600}
  .extra{left:80px;width:450px;text-align:center;font-size:15px;line-height:19.7px}
  .extra b{font-weight:600}

  .price-card{left:590px;width:220px;height:96px;border:1.5px solid var(--band-dark)}
  .price-card .day{height:28px;background:var(--band);color:var(--white);
    font-family:"Libre Baskerville",Georgia,serif;font-size:14px;
    display:flex;align-items:center;justify-content:center;position:relative}
  .price-card .day::before{content:"";position:absolute;left:3px;top:0;width:5px;height:14px;background:var(--white);
    clip-path:polygon(0 0,100% 0,100% 100%,50% 75%,0 100%)}
  .price-card .amount{height:66px;display:flex;align-items:center;justify-content:center;
    font-family:"Libre Baskerville",Georgia,serif;font-size:14px;color:var(--price)}

  .additional-band{left:25px;top:621px;width:811px;height:31px;border-radius:9px;background:var(--band);
    color:var(--white);font-family:"Libre Baskerville",Georgia,serif;font-size:16.5px;
    display:flex;align-items:center;justify-content:center}

  .tile{overflow:hidden;border:1px solid #8a8a8a}
  .tile-photo{position:absolute;inset:0}
  .tile-text{position:absolute;color:var(--white);font-family:"Libre Baskerville",Georgia,serif;
    font-size:13px;line-height:19.5px;text-shadow:0 0 3px rgba(0,0,0,.35)}
  .tile-title{font-weight:700;font-size:15.5px;line-height:23px}
  .tile-price{position:absolute;color:var(--white);font-family:"Libre Baskerville",Georgia,serif;font-weight:700;font-size:14px}
  .fixtures{display:grid;grid-template-columns:268px auto;padding-left:28px}

  .footer-note{left:0;width:862px;top:1130px;text-align:center;font-family:"Libre Baskerville",Georgia,serif;
    font-weight:700;font-size:13px;color:var(--ink)}
  .crop{background:#000}
</style>
</head>
<body>

  <div class="abs hero" role="img" aria-label="Bride and groom sharing a first dance in a ballroom with low fog"></div>
  <div class="abs hero-haze"></div>
  <div class="abs brand"><span class="brand-dot"></span>Brightloom Events</div>
  <div class="abs contact">
    # 888.555.0142<br>
    brightloomevents.example<br>
    hello@brightloomevents.example<br>
    Instagram- @brightloomevents.example
  </div>
  <div class="abs services-line">DJ | LIGHTING | PRO AUDIO | VISUAL</div>

  <div class="abs package-band">5 Hour DJ/MC Wedding Reception Package</div>

  <div class="abs includes">
    <h2>This package includes:</h2>
    Formally attired &amp; live mixing DJ<br>
    Emcee hosting all announcements<br>
    Powered speaker sound system<br>
    Wireless microphones for toasts speeches<br>
    In-person consultation to discuss event details<br>
    Online access to planning forms &amp; music database<br>
    Upto 6 hours of continuous entertainment
  </div>
  <div class="abs extra" style="top:480px">
    Ceremony music (<b>included</b>)<br>
    (includes sound equipment, wireless mic &amp; ceremony music)
  </div>
  <div class="abs extra" style="top:539px">
    Cocktail hour music (<b>included</b>)<br>
    (includes music in cocktail hour area)
  </div>

  <div class="abs price-card" style="top:288px"><div class="day">Monday-Thursday</div><div class="amount">$1295</div></div>
  <div class="abs price-card" style="top:394px"><div class="day">Friday &amp; Sunday</div><div class="amount">$1395</div></div>
  <div class="abs price-card" style="top:499px"><div class="day">Saturday</div><div class="amount">$1495</div></div>

  <div class="abs additional-band">Additional services (when booked with DJ package)</div>

  <div class="abs tile" style="left:50px;top:663px;width:375px;height:147px">
    <div class="tile-photo" role="img" aria-label="Reception room with warm uplighting" style="background:linear-gradient(160deg,#8a6a60,#5e4a47 60%,#3e3434)"></div>
    <div class="tile-text" style="left:7px;top:33px;width:365px">
      <div class="tile-title">Room uplighting (colour of your choice)</div>
      <div class="fixtures"><span>20 fixtures (med-large room)</span><span>$400</span>
      <span>16 fixtures (med-large room)</span><span>$350</span>
      <span>12 fixtures (med-large room)</span><span>$300</span></div>
    </div>
  </div>

  <div class="abs tile" style="left:438px;top:663px;width:372px;height:147px">
    <div class="tile-photo" role="img" aria-label="Pin-spot lit centerpieces in a draped ballroom" style="background:linear-gradient(160deg,#b9a2bd,#9a87a2 55%,#8c7e93)"></div>
    <div class="tile-text" style="left:24px;top:40px;width:240px">
      <div class="tile-title">Pin-spot lighting</div>
      (wedding cake/centerpieces/<br>sweetheart table etc.)
    </div>
    <div class="tile-price" style="left:309px;top:41px">$30+</div>
  </div>

  <div class="abs tile" style="left:49px;top:819px;width:374px;height:146px">
    <div class="tile-photo" role="img" aria-label="Ballroom with monogram projected on the wall" style="background:linear-gradient(160deg,#8d8585,#6d6564 55%,#4f4846)"></div>
    <div class="tile-text" style="left:24px;top:34px;width:260px">
      <div class="tile-title">Dance floor decal/<br>Gobo Monogram</div>
      (Bride &amp; groom’s names appear<br>on the wall or dance floor)
    </div>
    <div class="tile-price" style="left:306px;top:63px">$250+</div>
  </div>

  <div class="abs tile" style="left:436px;top:819px;width:375px;height:146px">
    <div class="tile-photo" role="img" aria-label="Couple on a white dance floor with a name decal" style="background:linear-gradient(160deg,#7d6c66,#5b4b47 55%,#6f6560)"></div>
    <div class="tile-text" style="left:30px;top:42px;width:260px">
      <div class="tile-title">Seamless white dance floor<br>with decal</div>
      (square or round)
    </div>
    <div class="tile-price" style="left:289px;top:66px">$1000+</div>
  </div>

  <div class="abs tile" style="left:244px;top:974px;width:374px;height:147px">
    <div class="tile-photo" role="img" aria-label="Couple embracing beside indoor cold sparkler fountains" style="background:linear-gradient(120deg,#9a8a88,#6b6466 45%,#4a4a52)"></div>
    <div class="tile-text" style="left:0;width:374px;top:64px;text-align:center">
      <div class="tile-title">Indoor safe sparkler effect</div>
    </div>
  </div>

  <div class="abs footer-note">We offer a wide range of additional services. Please contact us for more info &amp; pricing.</div>

  <div class="abs crop" style="left:24px;top:0;width:1px;height:24px"></div>
  <div class="abs crop" style="left:812px;top:24px;width:30px;height:1px"></div>
  <div class="abs crop" style="left:24px;top:1152px;width:1px;height:40px"></div>
  <div class="abs crop" style="left:836px;top:1152px;width:1px;height:30px"></div>

</body>
</html>
```